Birchwater Ridge Electrical, needs business cards asap!

An electrical business, been in the trade for 10 to 12 years. Based on a partner business, names Dale Brixworth and Rk Tolly. Would like a potential logo drawn up to use on all products as well. It's a new company starting in the spring.
This is my first time using this site to make business cards. I can tell you a little about the business, I have been working as an electrician for 10 years for a company and have done courses to upgrade my skills, I'm open minded, and am very personable. Over the years I just have had it working for "the man" and want to try it on my own. I am extremely hard worker I work long hours.

again anything is so appreciative,

Thank you

Dale

Target Market(s)

Small town, contractors, other business owners,

Industry/Entity Type

Electrical

Contact Information for Business Card

Simple but classy

Font styles to use
Serif

Colors
ffc214
000000

Requirements
Must have
• Phone 705-418-9356
• Email birchwaterridgeelectrical@voltmail.test
• Address 14 Fenwick street alder bend on x9q 3k9
• Name of company ridge birchwater electrical
• Name of owners Dale Brixworth and rk tolly
• ECRA/ESA 4386192
Nice to have
• A potential logo which can be used on clothing trucks etc if no logo thats ok.

```html
<!DOCTYPE html>
<html lang="en">
<head>
<meta charset="utf-8">
<title>Birchwater Ridge Electrical – Business Cards</title>
<link href="https://fonts.googleapis.com/css2?family=Arimo:wght@400;700&display=swap" rel="stylesheet">
<style>
  :root {
    --brand-yellow: #ffc214;
    --brand-yellow-deep: #fdb515;
    --brand-black: #000000;
    --black-soft: #141414;
    --white: #ffffff;
    --label-gold: #b5860f;
    --label-amber: #e0a11a;
  }
  * { margin: 0; padding: 0; box-sizing: border-box; }
  html, body {
    width: 1000px;
    height: 1200px;
    overflow: hidden;
    background: var(--white);
    font-family: "Arimo", Arial, sans-serif;
  }
  .card {
    position: absolute;
    left: 15px;
    width: 973px;
  }
  .card--front { top: 42px; height: 553px; }
  .card--back  { top: 600px; height: 553px; }

  .card__face {
    position: absolute;
    left: 0; top: 0;
    width: 100%;
    height: 496px;
  }
  .card--front .card__face {
    background: linear-gradient(135deg, var(--brand-yellow) 0%, var(--brand-yellow-deep) 50%, var(--brand-yellow) 100%);
  }
  .card--back .card__face {
    height: 487px;
    background: linear-gradient(135deg, var(--black-soft) 0%, var(--brand-black) 55%, var(--black-soft) 100%);
  }

  .card__band {
    position: absolute;
    left: 0; bottom: 0;
    width: 100%;
  }
  .card--front .card__band { height: 57px; background: var(--brand-black); color: var(--white); }
  .card--back .card__band  { height: 66px; background: var(--brand-yellow); color: var(--brand-black); }

  .wordmark {
    position: absolute;
    left: 115px;
    top: 176px;
    width: 320px;
    font-weight: 700;
    font-size: 37px;
    line-height: 39px;
    text-transform: uppercase;
    letter-spacing: -0.5px;
    text-align: center;
  }
  .card--front .wordmark { color: var(--brand-black); }
  .card--back .wordmark  { color: var(--white); top: 172px; }

  .person-name {
    position: absolute;
    font-weight: 700;
    font-size: 41px;
    color: var(--white);
    letter-spacing: -0.5px;
    white-space: nowrap;
  }
  .card--front .person-name { left: 552px; top: 210px; }
  .card--back .person-name  { left: 552px; width: 375px; text-align: center; top: 208px; }

  .contact {
    position: absolute;
    left: 553px;
    font-size: 17px;
    line-height: 23px;
    color: var(--white);
    letter-spacing: -0.6px;
    white-space: nowrap;
  }
  .card--front .contact { top: 392px; }
  .card--back .contact  { top: 390px; }
  .contact__label { color: var(--label-gold); }
  .card--back .contact__label { color: var(--label-amber); }
  .contact__line--phone { padding-left: 5px; }

  .email {
    position: absolute;
    left: 555px;
    font-size: 17px;
    letter-spacing: 0.4px;
    white-space: nowrap;
  }
  .card--front .email { top: 19px; }
  .card--back .email  { top: 26px; }
</style>
</head>
<body>

  <section class="card card--front">
    <div class="card__face" role="img" aria-label="Yellow geometric triangle pattern background"></div>
    <div class="wordmark">Birchwater<br>Ridge<br>Electrical</div>
    <h1 class="person-name">Dale Brixworth</h1>
    <div class="contact">
      <p class="contact__line contact__line--phone"><span class="contact__label">Phone</span> : 705-418-9356</p>
      <p class="contact__line"><span class="contact__label">Address</span> : 14 Fenwick street alder bend on x9q 3k9</p>
      <p class="contact__line">ECRA/ESA 4386192</p>
    </div>
    <div class="card__band">
      <p class="email">Email birchwaterridgeelectrical@voltmail.test</p>
    </div>
  </section>

  <section class="card card--back">
    <div class="card__face" role="img" aria-label="Black geometric triangle pattern background"></div>
    <div class="wordmark">Birchwater<br>Ridge<br>Electrical</div>
    <h1 class="person-name">rk tolly</h1>
    <div class="contact">
      <p class="contact__line contact__line--phone"><span class="contact__label">Phone</span> : 705-418-9356</p>
      <p class="contact__line"><span class="contact__label">Address</span> : 14 Fenwick street alder bend on x9q 3k9</p>
      <p class="contact__line">ECRA/ESA 4386192</p>
    </div>
    <div class="card__band">
      <p class="email">Email birchwaterridgeelectrical@voltmail.test</p>
    </div>
  </section>

</body>
</html>
```